Copperleaf Grill
there is none
Copperleaf Grill -
Simple
Danielle Whitcomb
Proprietor
318 Ferrand Street New Orleans, LA 70119
dwhitcomb@copperleaf-eats.com
www.copperleaf-eats.com
Use the same font of Grill and New Orleans for information on card
Just put the logo and website on the back of the card

```html
<!DOCTYPE html>
<html lang="en">
<head>
<meta charset="utf-8">
<title>Copperleaf Grill – Business Cards</title>
<link href="https://fonts.googleapis.com/css2?family=PT+Sans:wght@400;700&display=swap" rel="stylesheet">
<style>
  :root {
    --maroon: #7d2634;
    --black: #0b0a0a;
    --white: #ffffff;
    --ink: #2a2a2a;
    --stage: #ffffff;
    --edge: #d6d6d6;
  }
  * { margin: 0; padding: 0; box-sizing: border-box; }
  html, body { width: 1200px; height: 742px; overflow: hidden; background: var(--stage); }
  body { position: relative; font-family: "PT Sans", sans-serif; }

  .card {
    position: absolute;
    width: 566px;
    height: 329px;
    overflow: hidden;
  }
  .card--front { left: 20px; top: 43px; background: var(--white); border: 1px solid var(--edge); }
  .card--back-maroon { left: 600px; top: 43px; width: 576px; background: var(--maroon); }
  .card--back-black { left: 314px; top: 391px; width: 569px; background: var(--black); }

  .top-band { position: absolute; left: 0; top: 0; width: 100%; height: 40px; }

  .brand-name {
    position: absolute;
    font-family: "PT Sans", sans-serif;
    font-weight: 700;
    white-space: nowrap;
  }
  .card--front .brand-name { left: 40px; top: 74px; font-size: 30px; color: var(--black); }
  .card--back-maroon .brand-name,
  .card--back-black .brand-name {
    left: 0; width: 100%; text-align: center; top: 128px; font-size: 38px;
  }
  .card--back-maroon .brand-name { color: var(--black); }
  .card--back-black .brand-name { color: var(--white); }

  .holder { position: absolute; left: 226px; top: 170px; color: var(--maroon); }
  .holder-name { font-size: 20px; line-height: 1.1; }
  .holder-title { font-size: 13px; margin-top: 3px; }

  .contact {
    position: absolute; left: 20px; top: 203px;
    font-size: 13px; line-height: 20px; color: var(--ink);
    list-style: none;
  }

  .website {
    position: absolute; left: 0; width: 100%; text-align: center;
    top: 282px; font-size: 15px; color: var(--white);
  }
  .card--back-black .website { top: 277px; }
</style>
</head>
<body>

  <section class="card card--front" aria-label="Card front">
    <svg class="top-band" viewBox="0 0 566 40" preserveAspectRatio="none" aria-hidden="true">
      <path d="M0 0 H566 V30 C430 14 250 10 0 12 Z" fill="var(--maroon)"/>
    </svg>
    <div class="brand-name">Copperleaf Grill</div>
    <div class="holder">
      <div class="holder-name">Danielle Whitcomb</div>
      <div class="holder-title">Proprietor</div>
    </div>
    <ul class="contact">
      <li>318 Ferrand Street</li>
      <li>New Orleans, LA 70119</li>
      <li>Phone: 504.555.0142</li>
      <li>Cell: 225.555.0187</li>
      <li>Email: dwhitcomb@copperleaf-eats.com</li>
    </ul>
  </section>

  <section class="card card--back-maroon" aria-label="Card back, maroon">
    <div class="brand-name">Copperleaf Grill</div>
    <div class="website">www.copperleaf-eats.com</div>
  </section>

  <section class="card card--back-black" aria-label="Card back, black">
    <div class="brand-name">Copperleaf Grill</div>
    <div class="website">www.copperleaf-eats.com</div>
  </section>

</body>
</html>
```